Crestline Lending Group Business Cards

We are looking to revamp the current business cards each of our locations uses. We are a lending company that specializes in personal loans, title loans, and tax services. We have locations in New Mexico, Texas, and Oklahoma.

We would like a cleaner, sleeker look while still highlighting what we offer. Title Loans, Personal Loans & Tax Services. We also want to include our referral fee somewhere on the card. We would like to see an English option as well as a Spanish option for the cards.

PLEASE NOTE: Some business cards do not include the employee's name but just the store's location, while others will include both.

These are double-sided business cards, and we would like to see proof if possible. I have included proofs of our current business cards for you to review below, as well as our company logo. Feel free to get creative with the logo, etc! Colors should match the logo; however, you do not need to use all of our logo colors if you don't want to.

```html
<!DOCTYPE html>
<html lang="en">
<head>
<meta charset="utf-8">
<title>Crestline Lending Group – Business Cards</title>
<link rel="stylesheet" href="https://fonts.googleapis.com/css2?family=Montserrat:wght@400;500;700&family=Oswald:wght@600&display=swap">
<style>
  :root {
    --backdrop: #2b2e31;
    --green: #0e5a2e;
    --red: #c41e24;
    --ink: #222222;
    --paper: #ffffff;
    --edge: #1f6f9a;
  }
  * { box-sizing: border-box; margin: 0; padding: 0; }
  html, body { width: 1200px; height: 780px; overflow: hidden; }
  body {
    background: var(--backdrop);
    font-family: "Montserrat", sans-serif;
    display: flex;
    flex-direction: column;
    align-items: center;
    justify-content: center;
    gap: 40px;
  }
  .card {
    width: 560px;
    height: 320px;
    position: relative;
    border-radius: 4px;
    box-shadow: 0 6px 0 var(--edge), 0 14px 30px rgba(0,0,0,.45);
    overflow: hidden;
  }
  /* back side */
  .card--referral {
    background: linear-gradient(115deg, var(--green) 0%, var(--green) 30%, #7a2e2a 58%, var(--red) 82%);
    color: var(--paper);
  }
  .referral-heading, .referral-offer {
    font-family: "Oswald", sans-serif;
    font-weight: 600;
    letter-spacing: 2px;
    position: absolute;
    font-size: 26px;
  }
  .referral-heading { top: 52px; left: 40px; }
  .referral-offer { bottom: 48px; right: 40px; }
  .brand {
    display: flex;
    align-items: center;
    gap: 10px;
    font-weight: 700;
  }
  .brand-dot {
    width: 14px; height: 14px; border-radius: 50%;
    flex: none;
  }
  .card--referral .brand {
    position: absolute;
    top: 50%; left: 50%;
    transform: translate(-50%, -50%);
    font-size: 26px;
    color: var(--paper);
    white-space: nowrap;
  }
  .card--referral .brand-dot { background: var(--paper); }

  /* front side */
  .card--contact { background: var(--paper); color: var(--ink); }
  .card--contact .brand {
    position: absolute;
    top: 56px; left: 36px;
    width: 210px;
    font-size: 22px;
    line-height: 1.15;
    color: var(--green);
  }
  .card--contact .brand-dot { background: var(--red); }
  .contact {
    position: absolute;
    top: 46px; right: 34px;
    width: 240px;
    font-size: 12.5px;
    line-height: 1.35;
  }
  .contact-address { margin-bottom: 12px; }
  .contact-list { list-style: none; }
  .contact-list li { display: flex; align-items: center; gap: 7px; }
  .contact-list svg { width: 11px; height: 11px; flex: none; fill: none; stroke: var(--green); stroke-width: 2; }
  .accent { color: var(--red); }
  .rule-top {
    position: absolute; top: 178px; right: 34px; width: 250px;
    height: 1.5px; background: var(--red);
  }
  .person { position: absolute; left: 36px; top: 218px; }
  .person-name { font-size: 19px; font-weight: 700; color: var(--green); }
  .person-title { font-size: 14px; }
  .rule-bottom {
    position: absolute; left: 36px; right: 34px; top: 268px;
    height: 1.5px; background: var(--red);
  }
  .services {
    position: absolute; left: 86px; top: 280px;
    font-size: 13.5px;
  }
  .services-label { color: var(--red); font-weight: 700; }
  .services-dot {
    display: inline-block; width: 7px; height: 7px; border-radius: 50%;
    background: var(--green); margin: 0 5px; vertical-align: middle;
  }
</style>
</head>
<body>

<section class="card card--referral" aria-label="Referral side">
  <p class="referral-heading">REFER A FRIEND</p>
  <div class="brand"><span class="brand-dot"></span>Crestline Lending Group</div>
  <p class="referral-offer">GET UP TO 100$</p>
</section>

<section class="card card--contact" aria-label="Contact side">
  <div class="brand"><span class="brand-dot"></span>Crestline Lending Group</div>

  <div class="contact">
    <p class="contact-address">450 Mesa Ridge Road, Suite B,<br>Alamo Springs, Texas 79012</p>
    <ul class="contact-list">
      <li><svg viewBox="0 0 12 12"><path d="M3 1l2 2-1 2q1.5 2 3 3l2-1 2 2-1.5 1.5Q5 11 1 3z"/></svg>(505) 555-0148</li>
      <li><svg viewBox="0 0 12 12"><rect x="1" y="2.5" width="10" height="7"/><path d="M1 3l5 4 5-4"/></svg>info@crestlinelending.com</li>
      <li><svg viewBox="0 0 12 12"><circle cx="6" cy="6" r="5"/><path d="M1 6h10M6 1q-3 5 0 10M6 1q3 5 0 10"/></svg>www.<span class="accent">crestlinelending</span>.com</li>
    </ul>
  </div>
  <div class="rule-top"></div>

  <div class="person">
    <p class="person-name">Elena <span class="accent">Ruiz</span></p>
    <p class="person-title">Branch Manager</p>
  </div>
  <div class="rule-bottom"></div>

  <p class="services"><span class="services-label">Services</span> : Title Loans<span class="services-dot"></span>Personal Loans<span class="services-dot"></span>Tax Services</p>
</section>

</body>
</html>
```